Corvallin Property Solutions need a business card design

Hello guys. We would need a business card design asap please.
We are a start up property investment business based in London UK specialised in buying, selling, managing and letting properties and helping distressed property owners.
The name of our Business is Corvallin, the logo symbolises the four fundamental elements of the world (earth, air, fire and water) and so it stands for strength, stability, longevity.
We would like the business card to communicate professionalism and reliability. Many many thanks indeed for your work.

Details:

1.) Marisol Dunkley
Property Investor
Mobile: +44(0)7700362517
Email: marisol.corvallin@quilbrook.example

2.) Tomas Brindle
Property Investor
Mobile: +44(0)7700845926
Email: tomas.corvallin@quilbrook.example

Industry/Entity Type

Investment

```html
<!DOCTYPE html>
<html lang="en">
<head>
<meta charset="utf-8">
<title>Corvallin Property Solutions — Business Card</title>
<link href="https://fonts.googleapis.com/css2?family=Jost:wght@500;600&family=Roboto+Condensed:wght@400;700&display=swap" rel="stylesheet">
<style>
  :root {
    --canvas-white: #ffffff;
    --panel-black: #000000;
    --brand-orange: #f6901e;
    --card-dark-top: #4b4b4c;
    --card-dark-bottom: #333334;
    --ink-white: #ffffff;
    --ink-grey: #464646;
    --mark-tone: #e8e8e8;
  }
  * { margin: 0; padding: 0; box-sizing: border-box; }
  html, body { width: 1200px; height: 900px; overflow: hidden; background: var(--canvas-white); }
  .canvas { position: relative; width: 1200px; height: 900px; background: var(--canvas-white); }

  .brand-panel {
    position: absolute; left: 0; top: 0; width: 382px; height: 900px;
    background: var(--panel-black);
  }
  .brand-lockup {
    position: absolute; left: 0; width: 382px; top: 350px; text-align: center;
    font-family: "Jost", sans-serif; color: var(--ink-grey);
  }
  .brand-mark { display: block; margin: 0 auto 40px; }
  .brand-name { font-size: 25px; font-weight: 600; letter-spacing: 1px; line-height: 1; }
  .brand-tagline { font-size: 12px; font-weight: 600; letter-spacing: 0.6px; margin-top: 8px; }

  .card {
    position: absolute; overflow: hidden;
    box-shadow: 0 14px 28px rgba(0,0,0,0.28);
  }
  .card-divider { position: absolute; width: 1.5px; background: var(--ink-white); }

  .card-front {
    left: 495px; top: 76px; width: 602px; height: 342px; border-radius: 30px;
    background: var(--brand-orange);
  }
  .front-heading {
    position: absolute; top: 27px; font-family: "Jost", sans-serif; font-weight: 500;
    font-size: 26px; letter-spacing: 0.8px; color: var(--ink-white); line-height: 1;
  }
  .front-heading.left { right: 312px; }
  .front-heading.right { left: 311px; }
  .front-lockup {
    position: absolute; left: 0; width: 100%; top: 122px; text-align: center;
    font-family: "Jost", sans-serif; color: var(--ink-white);
  }
  .front-lockup .brand-mark { margin-bottom: 18px; }
  .front-lockup .brand-name { font-size: 26px; }

  .card-back {
    left: 500px; top: 495px; width: 600px; height: 343px; border-radius: 28px;
    background: linear-gradient(180deg, var(--card-dark-top), var(--card-dark-bottom));
  }
  .holder { position: absolute; left: 21px; top: 19px; font-family: "Roboto Condensed", sans-serif; color: var(--ink-white); }
  .holder-name { font-size: 15px; font-weight: 700; }
  .holder-role { font-size: 14px; margin-top: 3px; }
  .contact {
    position: absolute; right: 20px; top: 20px; text-align: right;
    font-family: "Roboto Condensed", sans-serif; font-size: 13px; color: var(--ink-white);
  }
  .contact-line { display: flex; justify-content: flex-end; align-items: center; gap: 3px; height: 18px; }
  .contact-icon { width: 12px; height: 12px; }
  .back-lockup {
    position: absolute; left: 0; width: 100%; top: 95px; text-align: center;
    font-family: "Jost", sans-serif; color: var(--ink-white);
  }
  .back-lockup .brand-mark { margin-bottom: 26px; }
  .back-lockup .brand-name { font-size: 22px; }
  .back-lockup .brand-tagline { font-size: 10px; margin-top: 7px; }
</style>
</head>
<body>
<div class="canvas">

  <section class="brand-panel">
    <div class="brand-lockup">
      <svg class="brand-mark" width="80" height="80" viewBox="0 0 80 80" aria-hidden="true"><circle cx="40" cy="40" r="40" fill="var(--ink-grey)"/></svg>
      <div class="brand-name">CORVALLIN</div>
      <div class="brand-tagline">PROPERTY SOLUTIONS</div>
    </div>
  </section>

  <article class="card card-front">
    <span class="card-divider" style="left:300px; top:0; height:52px;"></span>
    <span class="card-divider" style="left:300px; top:291px; height:51px;"></span>
    <div class="front-heading left">PROPERTY</div>
    <div class="front-heading right">SOLUTIONS</div>
    <div class="front-lockup">
      <svg class="brand-mark" width="56" height="56" viewBox="0 0 56 56" aria-hidden="true"><circle cx="28" cy="28" r="28" fill="var(--ink-white)"/></svg>
      <div class="brand-name">CORVALLIN</div>
    </div>
  </article>

  <article class="card card-back">
    <span class="card-divider" style="left:299px; top:0; height:52px;"></span>
    <span class="card-divider" style="left:299px; top:293px; height:50px;"></span>
    <div class="holder">
      <div class="holder-name">Marisol Dunkley</div>
      <div class="holder-role">Property Investor</div>
    </div>
    <div class="contact">
      <div class="contact-line">
        <svg class="contact-icon" viewBox="0 0 12 12" aria-hidden="true"><circle cx="6" cy="6" r="5.3" fill="none" stroke="var(--ink-white)" stroke-width="1"/><rect x="4.2" y="2.8" width="3.6" height="6.4" rx="0.7" fill="none" stroke="var(--ink-white)" stroke-width="0.9"/></svg>
        <span>+44(0)7700362517</span>
      </div>
      <div class="contact-line">
        <svg class="contact-icon" viewBox="0 0 12 12" aria-hidden="true"><circle cx="6" cy="6" r="5.3" fill="none" stroke="var(--ink-white)" stroke-width="1"/><rect x="3" y="4" width="6" height="4.2" fill="none" stroke="var(--ink-white)" stroke-width="0.9"/><path d="M3 4 L6 6.4 L9 4" fill="none" stroke="var(--ink-white)" stroke-width="0.9"/></svg>
        <span>marisol.corvallin@quilbrook.example</span>
      </div>
    </div>
    <div class="back-lockup">
      <svg class="brand-mark" width="72" height="72" viewBox="0 0 72 72" aria-hidden="true"><circle cx="36" cy="36" r="36" fill="var(--mark-tone)"/></svg>
      <div class="brand-name">CORVALLIN</div>
      <div class="brand-tagline">PROPERTY SOLUTIONS</div>
    </div>
  </article>

</div>
</body>
</html>
```